Orthopedist website

We need a web design for a relaunch of this website: http://www.gelenkfix.at/
This website is for a orthopedist. Please fell free to create a modern and clean layout. The currently used colours need not to be used in the new design.
The website should transport reliability so that patients will call or contact the doctor for a treatment.
A specially logo is not available.
Reason: We will get a new logo which should be integrated into the design.
Reason: Customer will get a new logo (is ready soon).
The target market are patients from salzburg / austria which have orthopedic problems (hand, feet, backbone)
Doctor

```html
<!DOCTYPE html>
<html lang="de">
<head>
<meta charset="utf-8">
<title>GelenkFix – Orthopädie Salzburg</title>
<link rel="stylesheet" href="https://fonts.googleapis.com/css2?family=Lato:wght@300;400;700&family=Roboto:wght@400;500;700&display=swap">
<style>
  :root {
    --teal: #17bfb2;
    --teal-dark: #12a99d;
    --ink: #2f3237;
    --text: #4a4d52;
    --muted: #9a9ea3;
    --line: #e6e9ea;
    --bar: #23262b;
    --mint: #eef8f6;
    --page-bg: #f7f7f7;
    --white: #ffffff;
  }
  * { box-sizing: border-box; margin: 0; padding: 0; }
  html, body { width: 970px; height: 1200px; overflow: hidden; }
  body {
    background: var(--page-bg);
    font-family: "Roboto", Arial, sans-serif;
    color: var(--text);
    position: relative;
  }
  .page { position: absolute; left: 89px; top: 16px; width: 793px; height: 1184px; background: var(--white); }
  .abs { position: absolute; }

  /* top bar */
  .topbar { left: 0; top: 0; width: 793px; height: 28px; background: var(--bar); color: #d8dadc; font-size: 9px; }
  .topbar .ask { left: 20px; top: 9px; }
  .topbar .phone { left: 107px; top: 9px; color: var(--teal); }
  .topbar .mail { left: 176px; top: 9px; color: var(--teal); }
  .topbar .mark { left: 141px; top: 26px; width: 50px; height: 2px; background: var(--teal); }
  .dots { display: flex; gap: 10px; }
  .dots span { width: 9px; height: 9px; border-radius: 50%; background: #a9acb0; }
  .topbar .dots { right: 22px; top: 10px; }

  /* header */
  .header { left: 0; top: 28px; width: 793px; height: 58px; background: var(--white); }
  .logo { left: 25px; top: 15px; font-family: "Lato", sans-serif; font-size: 23px; font-weight: 400; color: var(--teal); }
  .nav { left: 270px; top: 0; height: 58px; display: flex; }
  .nav a { display: block; width: 70px; line-height: 58px; text-align: center; font-size: 10px; color: var(--ink); text-decoration: none; border-left: 1px solid #f0f1f2; }
  .nav a.active { color: var(--teal); border-left: none; }

  /* hero */
  .hero { left: 0; top: 86px; width: 793px; height: 406px; overflow: hidden; }
  .hero-bg { position: absolute; inset: 0; background: linear-gradient(90deg, #cfeae5 0%, #dff2ee 45%, #eef8f6 100%); }
  .hero-photo { left: 439px; top: 119px; width: 354px; height: 226px; background: linear-gradient(135deg, #f4f8f8 0%, #dfe7ea 55%, #c9d4d8 100%); }
  .hero h1 { left: 0; width: 520px; top: 180px; text-align: center; font-family: "Lato", sans-serif; font-weight: 300; font-size: 32px; color: var(--ink); }
  .hero h1 em { font-style: normal; color: var(--teal); }
  .hero .lead { left: 80px; width: 360px; top: 238px; text-align: center; font-family: "Lato", sans-serif; font-weight: 300; font-size: 16px; line-height: 19px; color: var(--ink); }
  .btn { background: var(--teal); color: var(--white); font-size: 10px; font-weight: 500; border-radius: 2px; text-align: center; }
  .hero .btn { left: 162px; top: 309px; width: 119px; height: 27px; line-height: 27px; }

  /* intro */
  .intro { left: 0; top: 492px; width: 793px; height: 99px; background: var(--white); }
  .intro h2 { left: 0; width: 793px; top: 30px; text-align: center; font-family: "Lato", sans-serif; font-weight: 300; font-size: 26px; color: var(--ink); }
  .intro .tri { top: 41px; width: 0; height: 0; border-top: 6px solid transparent; border-bottom: 6px solid transparent; }
  .intro .tri.l { left: 174px; border-left: 10px solid var(--teal); }
  .intro .tri.r { left: 609px; border-right: 10px solid var(--teal); }
  .intro p { left: 0; width: 793px; top: 73px; text-align: center; font-size: 9px; color: var(--muted); }

  /* cards */
  .cards { left: 0; top: 591px; width: 793px; height: 280px; background: var(--mint); }
  .card { background: var(--white); box-shadow: 0 1px 2px rgba(0,0,0,.05); }
  .doctor { left: 14px; top: 38px; width: 378px; height: 208px; }
  .doctor .photo { left: 8px; top: 24px; width: 116px; height: 157px; background: linear-gradient(180deg, #c9cccf 0%, #b5b0aa 55%, #e8e8e8 100%); }
  .doctor h3 { left: 150px; top: 18px; font-family: "Lato", sans-serif; font-weight: 300; font-size: 16px; color: var(--ink); }
  .doctor .role { left: 150px; top: 40px; width: 210px; font-size: 10px; line-height: 16px; color: var(--muted); font-weight: 500; }
  .doctor .rule { left: 150px; top: 82px; width: 87px; height: 1px; background: var(--teal); }
  .doctor .bio { left: 150px; top: 97px; width: 210px; font-size: 10px; line-height: 16px; color: var(--text); font-weight: 500; }
  .social { left: 150px; top: 138px; display: flex; gap: 5px; }
  .social span { width: 32px; height: 32px; border: 1px solid var(--line); box-shadow: 0 1px 2px rgba(0,0,0,.08); display: flex; align-items: center; justify-content: center; }
  .social i { width: 8px; height: 8px; background: #3a3d42; border-radius: 50%; display: block; }
  .social svg { display: block; }

  .hours { left: 405px; top: 38px; width: 175px; height: 208px; }
  .hours h3 { left: 16px; top: 16px; font-family: "Lato", sans-serif; font-weight: 300; font-size: 16px; color: var(--ink); }
  .hours p { left: 16px; top: 45px; width: 150px; font-size: 8.5px; line-height: 13px; color: var(--text); }
  .slot { left: 0; width: 175px; text-align: center; }
  .slot .day { display: inline-block; background: #eef0f1; font-size: 8px; padding: 3px 6px; color: var(--text); }
  .slot .time { display: block; margin-top: 4px; font-size: 15px; color: var(--teal); }
  .slot .time sup { font-size: 8px; }
  .hours .divider { left: 16px; top: 143px; width: 143px; height: 1px; background: var(--line); }

  .contact { left: 595px; top: 36px; width: 176px; height: 205px; background: var(--teal); color: var(--white); }
  .contact h3 { left: 18px; top: 26px; font-family: "Lato", sans-serif; font-weight: 300; font-size: 16px; }
  .crow { left: 0; width: 176px; border-top: 1px solid rgba(255,255,255,.18); font-size: 8.5px; font-weight: 700; line-height: 11px; }
  .crow svg { position: absolute; left: 20px; }
  .crow span { position: absolute; left: 50px; }

  /* cta */
  .cta { left: 0; top: 871px; width: 793px; height: 104px; background: var(--teal); }
  .cta p { left: 73px; top: 43px; font-family: "Lato", sans-serif; font-weight: 300; font-size: 16px; color: var(--white); }
  .cta .visit { left: 590px; top: 38px; width: 119px; height: 28px; background: var(--white); border-radius: 2px; font-size: 9px; color: var(--ink); }
  .cta .visit span { position: absolute; left: 12px; top: 9px; }
  .cta .visit .ico { position: absolute; right: 0; top: 0; width: 28px; height: 28px; background: #eef0f1; border-radius: 0 2px 2px 0; }

  /* pulse band */
  .pulse { left: 0; top: 975px; width: 793px; height: 154px; background: var(--white); }
  .pulse-art { position: absolute; left: 24px; top: 20px; width: 745px; height: 114px; background: linear-gradient(180deg, #ffffff 0%, #e6f6f4 50%, #ffffff 100%); }

  /* footer */
  .footer { left: 0; top: 1129px; width: 793px; height: 55px; background: var(--bar); }
  .footer small { position: absolute; left: 20px; top: 23px; font-size: 8.5px; color: #c9cbce; }
  .footer .dots { right: 70px; top: 24px; }
  .footer .dots span { background: #6f7378; }
  .totop { right: 20px; top: 13px; width: 28px; height: 28px; background: #f1f1f1; border-radius: 2px; }
</style>
</head>
<body>
<div class="page">

  <div class="abs topbar">
    <span class="abs ask">Have any questions?</span>
    <span class="abs phone">&#9990; 123 456 7890</span>
    <span class="abs mail">&#9993; noreply@domain.com</span>
    <span class="abs mark"></span>
    <div class="abs dots"><span></span><span></span><span></span><span></span><span></span><span></span><span></span><span></span><span></span></div>
  </div>

  <header class="abs header">
    <div class="abs logo">GelenkFix</div>
    <nav class="abs nav">
      <a class="active" href="#">Home</a>
      <a href="#">Navigation</a>
      <a href="#">Navigation</a>
      <a href="#">Navigation</a>
      <a href="#">Navigation</a>
      <a href="#">Navigation</a>
      <a href="#">Navigation</a>
    </nav>
  </header>

  <section class="abs hero">
    <div class="hero-bg" role="img" aria-label="Bright clinic interior in soft mint tones"></div>
    <div class="abs hero-photo" role="img" aria-label="Two doctors examining an X-ray"></div>
    <h1 class="abs"><em>Welcome to</em>GelenkFix</h1>
    <p class="abs lead">We Are Orthopedist We Are Orthopedist<br>We Are Orthopedist</p>
    <div class="abs btn">Make an appointment</div>
  </section>

  <section class="abs intro">
    <span class="abs tri l"></span>
    <h2 class="abs">The Highest Standard of Your Care</h2>
    <span class="abs tri r"></span>
    <p class="abs">Morbi in sem quis dui placerat ornare. Pellentesque odio nisi, euismod in, pharetra a, ultricies in, diam.</p>
  </section>

  <section class="abs cards">
    <article class="abs card doctor">
      <div class="abs photo" role="img" aria-label="Portrait of the doctor"></div>
      <h3 class="abs">Dr. Lukas Berndorfer</h3>
      <p class="abs role">Facharzt für Orthopädie und Orthopädische Chirurgie</p>
      <span class="abs rule"></span>
      <p class="abs bio">Der persönliche Kontakt ist immer wichtig. Lernen Sie hier unser Praxisteam kennen.</p>
      <div class="abs social">
        <span><svg width="11" height="8" viewBox="0 0 11 8"><rect x="0.5" y="0.5" width="10" height="7" fill="none" stroke="#3a3d42"/><path d="M0.5 0.5 L5.5 4.5 L10.5 0.5" fill="none" stroke="#3a3d42"/></svg></span>
        <span><i></i></span>
        <span><i></i></span>
        <span><i></i></span>
      </div>
    </article>

    <article class="abs card hours">
      <h3 class="abs">Opening hours</h3>
      <p class="abs">Vitae adipiscing turpis. Aenean ligula nibh, molestie id viverra a, dapibus at dolor.</p>
      <div class="abs slot" style="top:97px"><span class="day">Monday - Friday</span><span class="time">8<sup>00</sup> - 16<sup>00</sup></span></div>
      <span class="abs divider"></span>
      <div class="abs slot" style="top:152px"><span class="day">Saturday</span><span class="time">8<sup>00</sup> - 15<sup>00</sup></span></div>
    </article>

    <article class="abs contact">
      <h3 class="abs">Get in touch</h3>
      <div class="abs crow" style="top:62px;height:36px;border-top:none">
        <svg width="8" height="11" viewBox="0 0 8 11" style="top:6px"><path d="M4 0a4 4 0 0 1 4 4c0 3-4 7-4 7S0 7 0 4a4 4 0 0 1 4-4z" fill="#fff"/><circle cx="4" cy="4" r="1.5" fill="#17bfb2"/></svg>
        <span style="top:4px">gelenkfix<br>121 uhuhu uhuh<br>ghghg, hghgh, jhjhjh</span>
      </div>
      <div class="abs crow" style="top:104px;height:28px">
        <svg width="10" height="10" viewBox="0 0 10 10" style="top:8px"><path d="M2 0l2 2.5-1.2 1.3c.6 1.3 1.6 2.3 2.9 2.9L7 5.5 10 7.5 8.5 10C4 9.5.5 6 0 1.5z" fill="#fff"/></svg>
        <span style="top:9px">123 456 7890</span>
      </div>
      <div class="abs crow" style="top:132px;height:28px">
        <svg width="11" height="8" viewBox="0 0 11 8" style="top:10px"><rect width="11" height="8" fill="#fff"/><path d="M0 0 L5.5 4.5 L11 0" fill="none" stroke="#17bfb2"/></svg>
        <span style="top:9px">noreply@domain.com</span>
      </div>
      <div class="abs crow" style="top:160px;height:28px">
        <svg width="11" height="11" viewBox="0 0 11 11" style="top:8px"><path d="M4.5 6.5l2-2M3.5 5L2 6.5a2 2 0 0 0 2.8 2.8L6.3 7.8M7.5 6L9 4.5A2 2 0 0 0 6.2 1.7L4.7 3.2" fill="none" stroke="#fff" stroke-width="1.3" stroke-linecap="round"/></svg>
        <span style="top:9px">http://www.domain.com/</span>
      </div>
    </article>
  </section>

  <section class="abs cta">
    <p class="abs">Do you want to visit our clinic? Make an free appointment!</p>
    <div class="abs visit"><span>Sign up for a visit</span><div class="ico"><svg width="28" height="28" viewBox="0 0 28 28"><path d="M11 17l1-3 5-5 2 2-5 5z" fill="none" stroke="#8a8e93"/></svg></div></div>
  </section>

  <section class="abs pulse">
    <div class="pulse-art" role="img" aria-label="Decorative heartbeat line illustration in teal on a faint grid"></div>
  </section>

  <footer class="abs footer">
    <small>© 2014. All Rights Reserved.</small>
    <div class="abs dots"><span></span><span></span><span></span><span></span><span></span><span></span><span></span><span></span><span></span></div>
    <div class="abs totop"><svg width="28" height="28" viewBox="0 0 28 28"><path d="M10 16l4-4 4 4" fill="none" stroke="#8a8e93" stroke-width="1.3"/></svg></div>
  </footer>

</div>
</body>
</html>
```